Paul Sefton Personal Card

I am looking for a personal card that has my contact information on the front and then the url for my website on the back. I am a fan of minimal, modern design, but am very open minded to other styles. Both portrait and landscape designs are acceptable. The only other specification that I have is that some sort of graphic of a raven is present somewhere on the card (my last name 'Sefton' means raven in German).
Contact Information for Business Card
Paul Sefton
608.554.1893
paulwsefton@postvane.net
paulwsefton.com
Colors
Designer to choose colors to be used in the design.
Requirements
Must have
- Raven on some part of the card

```html
<!DOCTYPE html>
<html lang="en">
<head>
<meta charset="utf-8">
<title>Paul Sefton Personal Card</title>
<link rel="stylesheet" href="https://fonts.googleapis.com/css2?family=Open+Sans:wght@400&family=Nothing+You+Could+Do&display=swap">
<style>
  :root {
    --page-bg: #dcdedd;
    --card-frost: #eff1f0;
    --card-frost-deep: #e3e6e5;
    --card-edge: #c6cac9;
    --band-ink: #141414;
    --band-back: #8f9190;
    --raven-ink: #1b1b1b;
    --raven-back: #7d7f7e;
    --silver: #c4c4c4;
    --contact-text: #ececec;
    --icon-muted: #a0a0a0;
  }
  html, body {
    margin: 0;
    width: 1200px;
    height: 578px;
    overflow: hidden;
    background: var(--page-bg);
  }
  .canvas {
    position: relative;
    width: 1200px;
    height: 578px;
  }
  .card {
    position: absolute;
    top: 116px;
    width: 560px;
    height: 345px;
    border-radius: 16px;
    border: 1px solid var(--card-edge);
    background: linear-gradient(160deg, var(--card-frost) 0%, var(--card-frost-deep) 100%);
    overflow: hidden;
    box-sizing: border-box;
  }
  .card-front { left: 25px; }
  .card-back { left: 615px; }
  .card-face {
    position: absolute;
    inset: 0;
  }
  .card-back .card-face {
    transform: scaleX(-1);
  }
  .contact-band {
    position: absolute;
    left: 0;
    right: 0;
    top: 157px;
    height: 68px;
    background: var(--band-ink);
  }
  .card-back .contact-band { background: var(--band-back); }
  .raven-artwork {
    position: absolute;
    left: 8px;
    top: 0;
    width: 345px;
    height: 305px;
  }
  .owner-name {
    position: absolute;
    left: 76px;
    top: 176px;
    margin: 0;
    font-family: "Nothing You Could Do", cursive;
    font-weight: 400;
    font-size: 30px;
    line-height: 1;
    color: var(--silver);
    white-space: nowrap;
  }
  .card-back .owner-name { color: #e6e6e6; }
  .contact-list {
    position: absolute;
    left: 356px;
    top: 164px;
    margin: 0;
    padding: 0;
    list-style: none;
    font-family: "Open Sans", sans-serif;
    font-size: 13.5px;
    line-height: 17px;
    color: var(--contact-text);
    white-space: nowrap;
  }
  .contact-item {
    display: flex;
    align-items: center;
    gap: 10px;
  }
  .contact-icon {
    width: 11px;
    height: 11px;
    flex: none;
  }
</style>
</head>
<body>
<main class="canvas">
  <section class="card card-front" aria-label="Card front">
    <div class="card-face">
      <div class="contact-band"></div>
      <svg class="raven-artwork" viewBox="0 0 345 305" role="img" aria-label="Raven silhouette illustration with raised wings, standing across the contact band">
        <defs>
          <radialGradient id="raven-tone-front" cx="50%" cy="52%" r="50%">
            <stop offset="0%" stop-color="var(--raven-ink)" stop-opacity="0.95"/>
            <stop offset="65%" stop-color="var(--raven-ink)" stop-opacity="0.75"/>
            <stop offset="100%" stop-color="var(--raven-ink)" stop-opacity="0"/>
          </radialGradient>
        </defs>
        <ellipse cx="172" cy="160" rx="172" ry="150" fill="url(#raven-tone-front)"/>
      </svg>
      <h1 class="owner-name">Paul Sefton</h1>
      <ul class="contact-list">
        <li class="contact-item">
          <svg class="contact-icon" viewBox="0 0 16 16" aria-hidden="true">
            <rect x="4.5" y="1" width="7" height="14" rx="1.5" fill="none" stroke="var(--contact-text)" stroke-width="1.4"/>
            <line x1="7" y1="12.5" x2="9" y2="12.5" stroke="var(--contact-text)" stroke-width="1.4"/>
          </svg>
          <span>608.554.1893</span>
        </li>
        <li class="contact-item">
          <svg class="contact-icon" viewBox="0 0 16 16" aria-hidden="true">
            <rect x="1.5" y="3.5" width="13" height="9" fill="var(--contact-text)"/>
            <polyline points="1.5,3.5 8,9 14.5,3.5" fill="none" stroke="var(--band-ink)" stroke-width="1.2"/>
          </svg>
          <span>paulwsefton@postvane.net</span>
        </li>
        <li class="contact-item">
          <svg class="contact-icon" viewBox="0 0 16 16" aria-hidden="true">
            <circle cx="8" cy="8" r="6.5" fill="none" stroke="var(--icon-muted)" stroke-width="1.2"/>
            <ellipse cx="8" cy="8" rx="3" ry="6.5" fill="none" stroke="var(--icon-muted)" stroke-width="1"/>
            <line x1="1.5" y1="8" x2="14.5" y2="8" stroke="var(--icon-muted)" stroke-width="1"/>
          </svg>
          <span>www.paulwsefton.com</span>
        </li>
      </ul>
    </div>
  </section>

  <section class="card card-back" aria-label="Card back, mirrored view through the clear card">
    <div class="card-face">
      <div class="contact-band"></div>
      <svg class="raven-artwork" viewBox="0 0 345 305" role="img" aria-label="Reverse side of the raven silhouette illustration, seen through the card">
        <defs>
          <radialGradient id="raven-tone-back" cx="50%" cy="52%" r="50%">
            <stop offset="0%" stop-color="var(--raven-back)" stop-opacity="0.9"/>
            <stop offset="65%" stop-color="var(--raven-back)" stop-opacity="0.65"/>
            <stop offset="100%" stop-color="var(--raven-back)" stop-opacity="0"/>
          </radialGradient>
        </defs>
        <ellipse cx="172" cy="160" rx="172" ry="150" fill="url(#raven-tone-back)"/>
      </svg>
      <p class="owner-name">Paul Sefton</p>
      <ul class="contact-list">
        <li class="contact-item">
          <svg class="contact-icon" viewBox="0 0 16 16" aria-hidden="true">
            <rect x="4.5" y="1" width="7" height="14" rx="1.5" fill="none" stroke="var(--contact-text)" stroke-width="1.4"/>
            <line x1="7" y1="12.5" x2="9" y2="12.5" stroke="var(--contact-text)" stroke-width="1.4"/>
          </svg>
          <span>608.554.1893</span>
        </li>
        <li class="contact-item">
          <svg class="contact-icon" viewBox="0 0 16 16" aria-hidden="true">
            <rect x="1.5" y="3.5" width="13" height="9" fill="var(--contact-text)"/>
            <polyline points="1.5,3.5 8,9 14.5,3.5" fill="none" stroke="var(--band-back)" stroke-width="1.2"/>
          </svg>
          <span>paulwsefton@postvane.net</span>
        </li>
        <li class="contact-item">
          <svg class="contact-icon" viewBox="0 0 16 16" aria-hidden="true">
            <circle cx="8" cy="8" r="6.5" fill="none" stroke="var(--contact-text)" stroke-width="1.2"/>
            <ellipse cx="8" cy="8" rx="3" ry="6.5" fill="none" stroke="var(--contact-text)" stroke-width="1"/>
            <line x1="1.5" y1="8" x2="14.5" y2="8" stroke="var(--contact-text)" stroke-width="1"/>
          </svg>
          <span>www.paulwsefton.com</span>
        </li>
      </ul>
    </div>
  </section>
</main>
</body>
</html>
```